Marlow Crest Homes Needs Business Card Design

Looking for a unique modern business card to fit my new Logo.
Name: Dean Marlow
Company: Marlow Crest Homes, LLC
Tag Line: Forever Framed Right
Email: marlowcresthomes@mailvista.test
Phone: (253) 555-0187
Website: www.marlowcresthomes.test
License: MARLOCH462QT

```html
<!DOCTYPE html>
<html lang="en">
<head>
<meta charset="UTF-8">
<title>Marlow Crest Homes – Business Card</title>
<link rel="stylesheet" href="https://fonts.googleapis.com/css2?family=Montserrat:wght@400;500;800&display=swap">
<style>
  :root {
    --brand-blue: #3897cc;
    --ink: #111111;
    --paper: #ffffff;
    --backdrop: #e7e8ea;
  }
  * { box-sizing: border-box; margin: 0; padding: 0; }
  html, body { width: 1200px; height: 900px; overflow: hidden; }
  body {
    background: var(--backdrop);
    font-family: "Montserrat", Arial, sans-serif;
    position: relative;
  }
  .card {
    position: absolute;
    left: 250px;
    width: 700px;
    height: 400px;
    overflow: hidden;
    box-shadow: 0 6px 18px rgba(0,0,0,0.18);
  }
  .card-front { top: 30px; background: var(--brand-blue); }
  .card-back  { top: 470px; background: var(--paper); }

  .wordmark {
    position: absolute;
    display: flex;
    align-items: center;
    gap: 16px;
    font-weight: 800;
    text-transform: uppercase;
    letter-spacing: 1px;
    line-height: 1.05;
  }
  .wordmark-mark { width: 26px; height: 26px; flex: none; }
  .card-front .wordmark {
    left: 0; right: 0; top: 0; bottom: 0;
    justify-content: center;
    color: var(--paper);
    font-size: 40px;
  }
  .card-front .wordmark-mark { background: var(--paper); }
  .card-back .wordmark {
    left: 40px; top: 110px;
    width: 300px;
    color: var(--ink);
    font-size: 30px;
  }
  .card-back .wordmark-mark { background: var(--brand-blue); }

  .swoosh { position: absolute; left: 0; top: 0; width: 700px; height: 400px; }

  .divider {
    position: absolute;
    left: 362px; top: 44px;
    width: 2px; height: 210px;
    background: var(--brand-blue);
  }
  .details {
    position: absolute;
    left: 390px; top: 38px;
    color: var(--ink);
  }
  .person-name {
    color: var(--brand-blue);
    font-weight: 800;
    font-size: 28px;
    letter-spacing: 0.5px;
    text-transform: uppercase;
    line-height: 1.2;
  }
  .company { font-size: 14px; font-weight: 500; margin-top: 2px; }
  .tagline { font-size: 14px; font-weight: 500; margin-top: 14px; }
  .license { font-size: 14px; font-weight: 500; margin-top: 2px; }
  .contact-list { list-style: none; margin-top: 14px; }
  .contact-list li {
    display: flex; align-items: center; gap: 10px;
    font-size: 14px; font-weight: 500;
    margin-bottom: 6px;
  }
  .contact-icon { width: 16px; height: 16px; flex: none; fill: var(--brand-blue); }
</style>
</head>
<body>

<section class="card card-front" aria-label="Card front">
  <div class="wordmark">
    <span class="wordmark-mark"></span>
    <span>Marlow Crest Homes</span>
  </div>
</section>

<section class="card card-back" aria-label="Card back">
  <svg class="swoosh" viewBox="0 0 700 400" aria-hidden="true">
    <path d="M0,345 C300,345 520,300 700,232 L700,400 L0,400 Z" fill="#111111"/>
    <path d="M0,355 C300,355 520,310 700,240 L700,400 L0,400 Z" fill="#ffffff"/>
    <path d="M0,363 C300,363 520,318 700,246 L700,400 L0,400 Z" fill="#3897cc"/>
  </svg>

  <div class="wordmark">
    <span class="wordmark-mark"></span>
    <span>Marlow Crest Homes</span>
  </div>

  <div class="divider"></div>

  <div class="details">
    <h1 class="person-name">Dean Marlow</h1>
    <p class="company">Marlow Crest Homes, LLC</p>
    <p class="tagline">Forever Framed Right</p>
    <p class="license">MARLOCH462QT</p>
    <ul class="contact-list">
      <li>
        <svg class="contact-icon" viewBox="0 0 24 24" aria-hidden="true"><path d="M6.6 10.8a15.1 15.1 0 0 0 6.6 6.6l2.2-2.2a1 1 0 0 1 1-.25 11.4 11.4 0 0 0 3.6.57 1 1 0 0 1 1 1V20a1 1 0 0 1-1 1A17 17 0 0 1 3 4a1 1 0 0 1 1-1h3.5a1 1 0 0 1 1 1c0 1.25.2 2.45.57 3.57a1 1 0 0 1-.25 1z"/></svg>
        <span>(253) 555-0187</span>
      </li>
      <li>
        <svg class="contact-icon" viewBox="0 0 24 24" aria-hidden="true"><path d="M2 5h20v14H2z M3.5 6.5 12 13l8.5-6.5" fill="none" stroke="#3897cc" stroke-width="2"/><path d="M2 5h20L12 12z"/></svg>
        <span>marlowcresthomes@mailvista.test</span>
      </li>
      <li>
        <svg class="contact-icon" viewBox="0 0 24 24" aria-hidden="true"><circle cx="12" cy="12" r="10"/><path d="M2 12h20M12 2c3 3 3 17 0 20M12 2c-3 3-3 17 0 20" fill="none" stroke="#ffffff" stroke-width="1.5"/></svg>
        <span>www.marlowcresthomes.test</span>
      </li>
    </ul>
  </div>
</section>

</body>
</html>
```